依頼詳細
今回は、トップページデザインの募集になります。
レスポンシブデザインのサイトで、bootstrap4を利用しコーディングする予定になります。
デザイン幅は2000px、コンテンツの幅はbootstrap4デフォルトの1110pxを基準としてください。ただし最近のデザインの流行を取りいれて、フルワイドや、1200~15000px程度の幅のコンテンツをバランスよくレイアウトしてください。
コンテンツ配置は基本12分割になります。がデザインによっては、多少逸脱してもかまいません。
念のため、サンプルのPSDデータを添付しますので、参照ください。

本文のフォントはゴシック系は游ゴシック、メイリオ、明朝系は遊明朝でお願いします。
飾り文字はフリーフォントか、googleフォントを利用してください。

メイン画像部分・グローバルメニューは、ワイド適用でお願いします。

その他内容詳細に関しては、別添のExcel資料を参照してください。
不明点、質問などありましたらメッセージ等でご連絡ください。
ページ数
1ページ
希望イメージ
シンプル 複雑
単色 カラフル
暗い 明るい
日常 高級
遊び心 厳粛
未来的 伝統的
女性的 男性的
希望する色
黄・オレンジ系、グレー系
納品ファイル
• 高解像度JPG (.jpg)
• フォトショップ形式 (.psd)
補足説明
納品ファイルは、PDF及びクライアント表示確認用のJPGを準備お願いします。
※9月13日追記
本件クライアントのご提案選定に時間を要しておりまして、止むを得ず案件の期間を延長させていただきました。
デザイナー様各位にはご心配をお掛けしすみませんが、案件に問題はございませんのでご安心いただければと思います。
引き続き、どうぞ宜しくお願いいたします。

カラーや素材の入れ方が良かったです。

本件クライアントの確認に時間が掛かってしまいましたが、最終的にカラーや素材の使い方が良かったとのことで、mina-teru様を当選とさせていただきました。
皆様ご提案ありがとうございました。
今後ともどうぞ宜しくお願いいたします。

```html
<!DOCTYPE html>
<html lang="ja">
<head>
<meta charset="utf-8">
<title>森川スポーツ</title>
<link href="https://fonts.googleapis.com/css2?family=Noto+Sans+JP:wght@400;500;700;900&display=swap" rel="stylesheet">
<style>
:root{
  --orange:#f39800;
  --orange-deep:#ea6a0c;
  --yellow:#fcc800;
  --peach:#fbd7a6;
  --dark:#2b2b2b;
  --dark-2:#3a3a3a;
  --gray:#777;
  --line:#e3e3e3;
  --bg-soft:#f5f5f5;
  --red:#d7261e;
  --white:#fff;
}
*{box-sizing:border-box;margin:0;padding:0}
html,body{width:1200px;height:2316px;overflow:hidden}
body{font-family:"Noto Sans JP",sans-serif;color:#333;background:var(--white);position:relative}
.abs{position:absolute}
/* header */
.site-header{position:absolute;left:0;top:0;width:1200px;height:148px;background:var(--white)}
.brand{position:absolute;left:110px;top:22px;display:flex;align-items:center;gap:10px}
.brand-square{width:26px;height:26px;background:var(--orange)}
.brand-name{font-size:26px;font-weight:900;color:var(--dark);letter-spacing:1px}
.brand-sub{position:absolute;left:146px;top:58px;font-size:11px;color:var(--gray)}
.header-contact{position:absolute;right:110px;top:18px;text-align:right}
.header-contact .label{font-size:11px;color:var(--gray)}
.header-contact .tel{display:flex;align-items:center;gap:6px;font-size:26px;font-weight:900;color:var(--orange-deep)}
.header-contact .hours{font-size:10px;color:var(--gray)}
.header-catch{position:absolute;top:108px;left:0;width:1200px;text-align:center;font-size:15px;font-weight:700;color:var(--red)}
.global-nav{position:absolute;top:148px;left:0;width:1200px;height:30px;background:var(--dark);display:flex;justify-content:center}
.global-nav a{color:#fff;font-size:11px;text-decoration:none;padding:0 22px;line-height:30px;border-right:1px solid #555}
.global-nav a:first-child{border-left:1px solid #555}
.global-nav a.current{background:var(--orange)}
/* sections */
.section{position:absolute;left:0;width:1200px;overflow:hidden}
.hero{top:178px;height:622px;background:var(--white)}
.bg-shapes{position:absolute;left:0;top:0}
.news-panel{position:absolute;left:220px;top:70px;width:760px;height:490px;background:var(--white);box-shadow:0 2px 10px rgba(0,0,0,.12);padding:24px 40px}
.heading{text-align:center}
.heading h2{font-size:18px;font-weight:700;color:#333}
.heading .en{font-size:10px;color:var(--orange);letter-spacing:1px}
.heading .bar{width:40px;height:2px;background:var(--orange);margin:6px auto 0}
.news-list{list-style:none;margin-top:22px}
.news-item{display:flex;align-items:center;height:74px;border-bottom:1px solid var(--line)}
.news-item time{width:110px;font-size:11px;color:var(--gray)}
.news-item p{flex:1;font-size:12px;line-height:1.6;color:#444}
.thumb{width:160px;height:54px;border-radius:2px}
.thumb-red{background:linear-gradient(135deg,#f2f2f2 0%,#e04438 55%,#b81e1e 100%)}
.thumb-white{background:linear-gradient(135deg,#fafafa,#d8d8d8 60%,#c13a32)}
.intro{top:800px;height:580px;background:var(--white)}
.intro-text{position:absolute;top:46px;width:1200px;text-align:center;font-size:17px;line-height:1.65;color:#555;font-weight:500}
.intro-photo{position:absolute;left:300px;top:150px;width:600px;height:130px;background:linear-gradient(90deg,#2a3a6a 0%,#c0c4d0 30%,#2f4a9a 55%,#e6e6e6 75%,#2aa0c8 100%)}
.order-box{position:absolute;left:330px;top:296px;width:540px;height:210px;background:#fff3d6;border:2px solid var(--orange)}
.order-title{height:36px;background:var(--orange);color:#fff;font-size:14px;font-weight:700;line-height:36px;padding-left:18px}
.order-photo{position:absolute;left:18px;top:50px;width:190px;height:110px;background:linear-gradient(135deg,#2c4aa0,#6f86c8 60%,#e6e6ee)}
.order-copy{position:absolute;left:230px;top:52px;width:290px;font-size:12px;line-height:1.7;color:#444}
.order-copy strong{color:var(--red);font-size:15px;display:block;margin-bottom:4px}
.order-btn{position:absolute;left:180px;top:166px;width:180px;height:28px;background:var(--orange-deep);color:#fff;font-size:12px;text-align:center;line-height:28px;border-radius:14px}
.recommend{top:1380px;height:460px;background:var(--bg-soft)}
.cards{position:absolute;left:220px;top:90px;display:flex;gap:20px}
.card{width:240px;height:270px;background:#fff;box-shadow:0 1px 4px rgba(0,0,0,.08)}
.card-img{height:160px}
.img-shoe{background:linear-gradient(135deg,#f6f6f6,#e23a2e 50%,#9e1414)}
.img-bag{background:linear-gradient(180deg,#f6f6f6,#2b2b2b 45%,#111)}
.img-pad{background:linear-gradient(180deg,#f6f6f6,#3a3a3a 45%,#151515)}
.card-body{padding:10px 12px}
.tag{display:inline-block;font-size:9px;color:#fff;padding:2px 6px;background:var(--dark)}
.tag.new{background:#3aa64a}
.card-title{font-size:12px;font-weight:700;margin-top:6px;line-height:1.5;height:36px}
.card-price{text-align:right;font-size:12px;color:var(--red);font-weight:700;margin-top:10px}
.more-btn{position:absolute;left:540px;top:390px;width:120px;height:30px;background:var(--orange);color:#fff;font-size:12px;text-align:center;line-height:30px;border-radius:15px}
.contact{top:1840px;height:380px;background:var(--white)}
.contact-catch{position:absolute;left:230px;top:34px;width:740px;height:38px;background:#fff;text-align:center;line-height:38px;font-size:17px;font-weight:700;color:#333}
.contact-box{position:absolute;left:260px;top:110px;width:680px;height:200px;background:var(--dark-2)}
.contact-brand{position:absolute;left:18px;top:18px;width:220px;height:110px;background:var(--dark);display:flex;align-items:center;justify-content:center;gap:8px}
.contact-brand .brand-name{color:#fff;font-size:20px}
.partners{position:absolute;left:18px;top:142px;display:flex;gap:12px}
.partner{width:104px;height:40px;background:#fff}
.contact-cols{position:absolute;left:258px;top:18px;display:flex;gap:14px}
.contact-card{width:196px;height:164px;border:1px solid #555;padding:10px;color:#fff;font-size:11px;line-height:1.6}
.contact-card .cta{margin-top:14px;height:44px;background:var(--orange);display:flex;align-items:center;justify-content:center;gap:6px;font-size:17px;font-weight:900}
.contact-card .cta.mail{font-size:13px;font-weight:700}
.site-footer{position:absolute;left:0;top:2220px;width:1200px;height:96px;background:var(--dark)}
.footer-nav{display:flex;justify-content:center;padding-top:24px}
.footer-nav a{color:#ddd;font-size:11px;text-decoration:none;padding:0 14px;border-right:1px solid #555}
.footer-nav a:last-child{border-right:none}
.copyright{text-align:center;color:#999;font-size:10px;margin-top:22px}
</style>
</head>
<body>

<header class="site-header">
  <div class="brand"><span class="brand-square"></span><span class="brand-name">森川スポーツ</span></div>
  <div class="brand-sub">レスリング用品専門店</div>
  <div class="header-contact">
    <div class="label">お電話でのお問い合わせ</div>
    <div class="tel">
      <svg width="22" height="22" viewBox="0 0 24 24"><path fill="#ea6a0c" d="M6.6 10.8a15 15 0 006.6 6.6l2.2-2.2a1 1 0 011-.25 11 11 0 003.6.6 1 1 0 011 1V20a1 1 0 01-1 1A17 17 0 013 4a1 1 0 011-1h3.5a1 1 0 011 1 11 11 0 00.6 3.6 1 1 0 01-.25 1z"/></svg>
      072-555-0142
    </div>
    <div class="hours">受付時間 10:00〜19:00（日祝休）</div>
  </div>
  <p class="header-catch">小学生から社会人まで幅広く対応！即日発送可能！全商品送料無料キャンペーン中！</p>
</header>

<nav class="global-nav">
  <a class="current" href="#">ホーム</a><a href="#">商品一覧</a><a href="#">オーダーメイド</a><a href="#">新着情報</a><a href="#">会社概要</a><a href="#">ご利用ガイド</a><a href="#">お問い合わせ</a>
</nav>

<section class="section hero">
  <svg class="bg-shapes" width="1200" height="622">
    <polygon points="0,0 420,0 0,330" fill="#f39800"/>
    <polygon points="0,330 0,622 260,622" fill="#fcc800"/>
    <polygon points="420,0 700,0 560,120" fill="#fbd7a6"/>
    <polygon points="780,0 1200,0 1200,360" fill="#fcc800"/>
    <polygon points="1200,360 1200,622 900,622" fill="#f39800"/>
    <polygon points="0,180 180,622 0,622" fill="#ea6a0c" opacity=".55"/>
    <polygon points="1000,622 1200,500 1200,622" fill="#ea6a0c" opacity=".6"/>
  </svg>
  <div class="news-panel">
    <div class="heading"><h2>お知らせ</h2><div class="en">INFORMATION</div><div class="bar"></div></div>
    <ul class="news-list">
      <li class="news-item"><time>2021.09.01</time><p>ショッピングサイトを新しくしました。<br>より快適にお買い物をお楽しみいただけます。</p><div class="thumb thumb-red" role="img" aria-label="レスリングシューズの写真"></div></li>
      <li class="news-item"><time>2021.08.20</time><p>2021年新作シューズ入荷しました。</p><div class="thumb thumb-red" role="img" aria-label="新作シューズの写真"></div></li>
      <li class="news-item"><time>2021.08.05</time><p>ショッピングサイトを新しくしました。<br>より快適にお買い物をお楽しみいただけます。</p><div class="thumb thumb-white" role="img" aria-label="シューズの写真"></div></li>
      <li class="news-item"><time>2021.07.18</time><p>2021年新作シューズ入荷しました。<br>人気モデルはお早めにどうぞ。</p><div class="thumb thumb-red" role="img" aria-label="シューズの写真"></div></li>
      <li class="news-item"><time>2021.07.01</time><p>夏季休業のお知らせを掲載しました。</p><div class="thumb thumb-white" role="img" aria-label="シューズの写真"></div></li>
    </ul>
  </div>
</section>

<section class="section intro">
  <svg class="bg-shapes" width="1200" height="580">
    <polygon points="0,0 260,0 0,260" fill="#f2f2f2"/>
    <polygon points="1200,80 1200,420 960,250" fill="#f2f2f2"/>
    <polygon points="80,580 300,380 380,580" fill="#f4f4f4"/>
  </svg>
  <p class="intro-text">レスリング関連商品は当店にお任せください。<br>取扱商品全て発送しております。<br>未掲載商品は、お気軽にお問い合わせください。</p>
  <div class="intro-photo" role="img" aria-label="シングレット・サポーター・ヘッドギアなどのレスリング用品の写真"></div>
  <div class="order-box">
    <div class="order-title">簡単3STEPでオーダーメイドができる！</div>
    <div class="order-photo" role="img" aria-label="オーダーメイドシューズの写真"></div>
    <div class="order-copy"><strong>自分だけのオリジナルを！</strong>カラー・素材・ネームを選ぶだけで、あなただけの一足やシングレットをお作りします。チーム単位のご注文も承ります。</div>
    <div class="order-btn">詳しくはこちら ›</div>
  </div>
</section>

<section class="section recommend">
  <svg class="bg-shapes" width="1200" height="460">
    <polygon points="0,0 200,0 0,200" fill="#ececec"/>
    <polygon points="1200,0 1200,260 1000,0" fill="#ececec"/>
    <polygon points="60,460 200,300 280,460" fill="#eeeeee"/>
  </svg>
  <div class="heading" style="position:absolute;top:24px;width:1200px"><h2>おすすめ商品</h2><div class="en">RECOMMEND ITEM</div><div class="bar"></div></div>
  <div class="cards">
    <article class="card"><div class="card-img img-shoe" role="img" aria-label="赤いレスリングシューズの写真"></div><div class="card-body"><span class="tag new">NEW ITEM</span><h3 class="card-title">レスリングシューズ マットモデル 赤×白</h3><div class="card-price">¥15,400（税込）</div></div></article>
    <article class="card"><div class="card-img img-bag" role="img" aria-label="黒いスポーツバッグの写真"></div><div class="card-body"><span class="tag">RECOMMEND</span><h3 class="card-title">キャリーバッグ 大容量タイプ</h3><div class="card-price">¥8,800（税込）</div></div></article>
    <article class="card"><div class="card-img img-pad" role="img" aria-label="黒い膝サポーターの写真"></div><div class="card-body"><span class="tag new">NEW ITEM</span><h3 class="card-title">ニーパッド 左右兼用</h3><div class="card-price">¥3,300（税込）</div></div></article>
  </div>
  <div class="more-btn">もっと見る ›</div>
</section>

<section class="section contact">
  <svg class="bg-shapes" width="1200" height="380">
    <polygon points="0,0 500,0 0,280" fill="#f39800"/>
    <polygon points="0,280 0,380 220,380" fill="#fcc800"/>
    <polygon points="700,0 1200,0 1200,300" fill="#fcc800"/>
    <polygon points="1200,300 1200,380 980,380" fill="#ea6a0c"/>
    <polygon points="500,0 700,0 600,90" fill="#fbd7a6"/>
  </svg>
  <p class="contact-catch">レスリング商品各種販売！スーツ・シューズのオーダーも！</p>
  <div class="contact-box">
    <div class="contact-brand"><span class="brand-square"></span><span class="brand-name">森川スポーツ</span></div>
    <div class="partners"><div class="partner"></div><div class="partner"></div></div>
    <div class="contact-cols">
      <div class="contact-card">ご注文・商品に関するお問い合わせ<br>お気軽にお電話ください
        <div class="cta"><svg width="18" height="18" viewBox="0 0 24 24"><path fill="#fff" d="M6.6 10.8a15 15 0 006.6 6.6l2.2-2.2a1 1 0 011-.25 11 11 0 003.6.6 1 1 0 011 1V20a1 1 0 01-1 1A17 17 0 013 4a1 1 0 011-1h3.5a1 1 0 011 1 11 11 0 00.6 3.6 1 1 0 01-.25 1z"/></svg>072-555-0142</div>
        <div style="margin-top:8px;font-size:10px;color:#bbb">受付 10:00〜19:00（日祝休）</div>
      </div>
      <div class="contact-card">オーダーメイドのご相談は<br>こちらからどうぞ
        <div class="cta mail"><svg width="18" height="14" viewBox="0 0 24 18"><rect x="1" y="1" width="22" height="16" fill="none" stroke="#fff" stroke-width="2"/><path d="M1 1l11 9 11-9" fill="none" stroke="#fff" stroke-width="2"/></svg>メールでお問い合わせ</div>
        <div style="margin-top:8px;font-size:10px;color:#bbb">24時間受付しております</div>
      </div>
    </div>
  </div>
</section>

<footer class="site-footer">
  <nav class="footer-nav"><a href="#">ホーム</a><a href="#">商品一覧</a><a href="#">オーダーメイド</a><a href="#">新着情報</a><a href="#">会社概要</a><a href="#">ご利用ガイド</a><a href="#">プライバシーポリシー</a><a href="#">お問い合わせ</a></nav>
  <p class="copyright">Copyright © 森川スポーツ All Rights Reserved.</p>
</footer>

</body>
</html>
```